Brona's Dwellings website

We need a simple website for our property investment business in the UK. We basically need our contact details and brief description.We have the company logo already done (via ArtVelo) so please use these:https://drive.google.com/drive/folders/1szJ3iRhelElZ40NIFT7w-c14MaY3Y_oV?usp=sharingYou could use some stock photos of UK houses for now.Let me know when to provide more detailed descriptions, etc

Coding

Coded - Design and coding required

Number of Pages Required

1 page

Colors

Designer to choose colors to be used in the design.

```html
<!DOCTYPE html>
<html lang="en">
<head>
<meta charset="utf-8">
<title>Brona's Dwellings — Property Management</title>
<link rel="stylesheet" href="https://fonts.googleapis.com/css2?family=Cormorant+Garamond:ital,wght@1,500&family=Poppins:wght@400;500&family=Roboto+Condensed:wght@400;500&family=Roboto+Slab:wght@400&display=swap">
<style>
:root{
  --ink:#111111;
  --text:#3a3a3a;
  --muted:#555555;
  --white:#ffffff;
  --rule:#d8d8d8;
  --panel:#1c1c1c;
  --dark:#2a2a2a;
  --footer:#1a1a1a;
  --bar:#0e0e0e;
  --accent:#1f3b57;
  --faint:#ececec;
}
*{margin:0;padding:0;box-sizing:border-box}
html,body{width:1200px;height:3239px;overflow:hidden;background:var(--white)}
body{position:relative;font-family:'Poppins',sans-serif;color:var(--text)}
.abs{position:absolute}
.script{font-family:'Cormorant Garamond',serif;font-style:italic;font-weight:500;color:var(--ink)}

/* header */
.site-header{left:0;top:0;width:1200px;height:92px;background:var(--white)}
.brand{left:142px;top:14px;width:131px;text-align:center;font-family:'Poppins',sans-serif;font-weight:500;font-size:15px;color:var(--ink);line-height:1.2}
.brand .mark{display:block;width:30px;height:30px;margin:0 auto 6px;background:var(--ink)}
.nav-link{top:44px;font-family:'Roboto Slab',serif;font-size:16px;color:var(--ink)}
.nav-link.active{border-bottom:1px solid var(--ink);padding-bottom:4px}
.nav-phone{left:900px;top:40px;font-family:'Poppins',sans-serif;font-size:17px;color:var(--ink);display:flex;align-items:center;gap:10px}

/* hero */
.hero{left:0;top:92px;width:1200px;height:594px}
.hero-photo{position:absolute;inset:0;background:linear-gradient(180deg,#e9d9c8 0%,#d8c49a 18%,#9aa46a 38%,#5d7a3a 60%,#6e5a3e 85%,#6b5442 100%);clip-path:path('M0 0 H1200 V420 Q600 760 0 420 Z')}
.hero-curve{position:absolute;left:0;top:0}
.hero-title{left:0;top:90px;width:1200px;text-align:center;font-family:'Roboto Condensed',sans-serif;font-weight:500;font-size:42px;line-height:51px;color:var(--ink)}
.slide-btn{top:232px;width:30px;height:24px;background:rgba(60,60,60,.8);border:1px solid #888;display:flex;align-items:center;justify-content:center}

/* about */
.about-photo{left:142px;top:771px;width:446px;height:446px;border:3px solid #3a3a3a;background:linear-gradient(160deg,#d9d2c4 0%,#b9b1a3 40%,#8a9a6e 75%,#6f8a4e 100%)}
.about-copy{left:630px;top:776px;width:418px}
.about-copy h2{font-size:38px;margin-bottom:14px}
.about-copy p{font-size:12.6px;line-height:23px;color:var(--muted);margin-bottom:9px}
.about-copy .lead{font-size:15.5px;font-weight:500;color:var(--ink);line-height:28px}

/* services */
.service{top:1277px;height:142px}
.service .plate{position:absolute;left:14px;top:0;width:150px;height:142px;background:var(--faint)}
.service .icon{position:absolute;left:60px;top:72px;width:52px;height:52px}
.service .label{position:absolute;left:140px;top:86px;font-size:18.5px;font-weight:500;color:#2a2a2a;line-height:24px}
.contact-line{left:0;width:1200px;text-align:center;font-size:38px}

/* why choose */
.why{left:0;top:1576px;width:1200px;height:444px;background:linear-gradient(100deg,#2b2b2b 0%,#1e1e1e 45%,#2c2c2c 100%);overflow:hidden}
.why h2{position:absolute;left:0;top:88px;width:1200px;text-align:center;font-size:38px;color:var(--white)}
.reason{position:absolute;color:var(--white);font-family:'Roboto Condensed',sans-serif}
.reason h3{font-size:17px;font-weight:500;line-height:20px}
.reason p{font-family:'Poppins',sans-serif;font-size:11px;line-height:17px;color:#e8e8e8}
.reason.right{text-align:right}
.badge{position:absolute;width:72px;height:72px;border-radius:50%;background:var(--white);border:3px solid #cfcfcf;display:flex;align-items:center;justify-content:center}
.hub{position:absolute;left:449px;top:293px;width:302px;height:151px;border-radius:151px 151px 0 0;background:var(--white);text-align:center}
.hub span{display:block;margin-top:86px;font-size:16px;font-weight:500;color:var(--ink)}

/* intro text */
.intro-title{left:0;top:2122px;width:1200px;text-align:center;font-size:38px}
.intro-body{left:150px;top:2168px;width:900px;text-align:center;font-size:12.6px;line-height:23px;color:var(--muted)}

/* question */
.desk{left:0;top:2466px;width:1200px;height:551px;background:linear-gradient(180deg,#f3f3f3 0%,#e6e6e6 100%)}
.card{left:268px;top:2561px;width:664px;height:465px;background:var(--white);box-shadow:0 2px 14px rgba(0,0,0,.08);text-align:center}
.card h2{margin-top:64px;font-size:38px;line-height:44px}
.card .bar{width:54px;height:2px;background:var(--accent);margin:16px auto 14px}
.card p{width:540px;margin:0 auto;font-size:12.6px;line-height:23px;color:var(--muted)}
.field{position:absolute;border:1px solid var(--rule);font-size:11px;color:#777;text-align:left;padding:12px 14px}
.submit{position:absolute;left:276px;top:360px;width:113px;height:35px;border-radius:18px;background:var(--ink);color:var(--white);font-size:14px;display:flex;align-items:center;justify-content:center;gap:8px}
.fold{position:absolute;left:0;bottom:0;width:36px;height:36px;background:linear-gradient(135deg,#fff 50%,#9a9a9a 50%)}

/* footer */
.site-footer{left:0;top:3017px;width:1200px;height:185px;background:var(--footer);color:var(--white)}
.contact-item{position:absolute;top:112px;display:flex;gap:12px;align-items:flex-start;font-size:14px;line-height:18px}
.foot-brand{position:absolute;left:860px;top:60px;width:200px;text-align:center;font-size:16px;font-weight:500;letter-spacing:1px}
.foot-brand .mark{display:block;width:44px;height:44px;margin:0 auto 12px;background:var(--white)}
.copy-bar{left:0;top:3202px;width:1200px;height:37px;background:var(--bar);color:var(--white);font-size:14px}
.copy-bar .note{position:absolute;left:142px;top:9px}
.social{position:absolute;top:7px;width:24px;height:24px;border-radius:50%}
</style>
</head>
<body>

<header class="abs site-header">
  <div class="abs brand"><span class="mark"></span>Brona's Dwellings</div>
  <a class="abs nav-link active" style="left:616px">Home</a>
  <a class="abs nav-link" style="left:692px">About Us</a>
  <a class="abs nav-link" style="left:790px">Contact Us</a>
  <div class="abs nav-phone">
    <svg width="26" height="26" viewBox="0 0 26 26"><circle cx="13" cy="13" r="11.5" fill="none" stroke="#111" stroke-width="1.6"/><path d="M10 7c-2 1-2 3-1 6s3 5 5 6c1 .4 2 0 3-1l-2-2-1 1c-1-.5-2-2-2.5-3l1-1-2-3z" fill="#111"/></svg>
    123-456-7890
  </div>
</header>

<section class="abs hero">
  <div class="hero-photo" role="img" aria-label="Aerial view of a green English town at sunrise with rows of houses and fields"></div>
  <svg class="hero-curve" width="1200" height="594" viewBox="0 0 1200 594"><path d="M0 420 Q600 760 1200 420 V445 Q600 760 0 445 Z" fill="#c9c9c9"/><path d="M0 445 Q600 760 1200 445 V594 H0 Z" fill="#fff"/></svg>
  <h1 class="abs hero-title">We Are Property Management Company In<br>London, UK</h1>
  <div class="abs slide-btn" style="left:4px"><svg width="8" height="10"><path d="M6 1 2 5l4 4" stroke="#fff" stroke-width="2" fill="none"/></svg></div>
  <div class="abs slide-btn" style="left:1162px"><svg width="8" height="10"><path d="M2 1l4 4-4 4" stroke="#fff" stroke-width="2" fill="none"/></svg></div>
</section>

<div class="abs about-photo" role="img" aria-label="Smiling estate agent in shirt and tie holding a folder in front of a house"></div>
<section class="abs about-copy">
  <h2 class="script">About Brona's Dwellings</h2>
  <p>Lorem ipsum dolor sit amet, consectetuer adipiscing elit, sed reederiam nonummy nibh euismod tincidunt ut laoreet dolore lor emsmagna aliquam erat volutpat. Ut wisi enim fdaad minim veniam, quis nostrud exerci tation ullamcorper suscipit lobortis nisl ut aliquip ex ea commodo consequat.</p>
  <p>Duis autem vel eum iriure dolor in hendrerit in vulputate velit re esse molestie consequat, vel illum dolore eu feugiat nulla facilisis at vero eros et accumsan et iusto odio dignissim qui blandit rer praesent luptatum zzril delenit augue duis dolore te feugait nulla ptatum zzril delenit augue duis dolo facilisi.</p>
  <p>Duis autem vel eum iriure dolor in hendrerit in vulputate velit re esse molestie consequat, vel illum dolore eu feugiat nulla facilisis at vero eros et .</p>
  <p class="lead">Get the support you need now. Contact our 24/7 support line to get started.</p>
</section>

<div class="abs service" style="left:142px;width:300px">
  <div class="plate"></div>
  <svg class="icon" viewBox="0 0 52 52"><path d="M8 24 26 10l18 14v22H8z" fill="#111"/><rect x="22" y="32" width="8" height="14" fill="#fff"/></svg>
  <div class="label" style="top:88px">Ground<br>Rent Collection</div>
</div>
<div class="abs service" style="left:476px;width:300px">
  <div class="plate"></div>
  <svg class="icon" style="left:42px" viewBox="0 0 52 52"><path d="M10 26 26 12l16 14v10H10z" fill="#111"/><path d="M4 38h30l12-6v8l-12 6H4z" fill="#111"/></svg>
  <div class="label" style="left:154px;top:92px">Property<br>Insurance</div>
</div>
<div class="abs service" style="left:780px;width:300px">
  <div class="plate"></div>
  <svg class="icon" style="left:50px" viewBox="0 0 52 52"><circle cx="34" cy="18" r="14" fill="none" stroke="#111" stroke-width="2"/><rect x="28" y="14" width="12" height="12" fill="#111"/><circle cx="14" cy="14" r="5" fill="#111"/><rect x="8" y="21" width="12" height="24" fill="#111"/></svg>
  <div class="label" style="left:155px;top:92px">Property<br>Accounting</div>
</div>
<p class="abs script contact-line" style="top:1442px">Contact Us Today - 123.456.7890</p>

<section class="abs why">
  <div class="abs" style="inset:0;background:linear-gradient(90deg,rgba(40,40,40,.0),rgba(20,20,20,.35))" role="img" aria-label="Businessman in a suit holding a hard hat beside a chalkboard of sketched charts"></div>
  <h2 class="script">Why Choose Us</h2>
  <svg class="abs" style="left:0;top:0" width="1200" height="444" viewBox="0 0 1200 444">
    <path d="M442 444 A158 158 0 0 1 758 444" fill="none" stroke="#bdbdbd" stroke-width="8"/>
    <g stroke="#bdbdbd" stroke-width="1.5" stroke-dasharray="3 3" fill="none">
      <path d="M540 262 L562 294"/><path d="M659 262 L640 294"/>
      <path d="M440 310 L491 330"/><path d="M759 310 L709 330"/>
      <path d="M392 368 L455 380"/><path d="M806 368 L745 380"/>
    </g>
    <g fill="#fff" stroke="#999" stroke-width="2">
      <circle cx="562" cy="294" r="5"/><circle cx="640" cy="294" r="5"/>
      <circle cx="491" cy="330" r="5"/><circle cx="709" cy="330" r="5"/>
      <circle cx="455" cy="380" r="5"/><circle cx="745" cy="380" r="5"/>
    </g>
  </svg>
  <div class="hub"><span>Brona's Dwellings</span></div>

  <div class="badge" style="left:504px;top:189px"><svg width="34" height="34" viewBox="0 0 34 34"><path d="M8 6c-3 2-3 6-1 11s6 9 10 11c2 1 4 0 5-2l-3-4-2 2c-2-1-4-4-5-6l2-2-3-5z" fill="#111"/></svg></div>
  <div class="badge" style="left:623px;top:189px"><svg width="34" height="34" viewBox="0 0 34 34"><circle cx="14" cy="14" r="6" fill="#111"/><rect x="5" y="22" width="18" height="10" rx="5" fill="#111"/></svg></div>
  <div class="badge" style="left:404px;top:237px"><svg width="34" height="34" viewBox="0 0 34 34"><circle cx="14" cy="19" r="8" fill="none" stroke="#111" stroke-width="5" stroke-dasharray="3 2"/><circle cx="25" cy="9" r="4" fill="none" stroke="#111" stroke-width="3"/></svg></div>
  <div class="badge" style="left:723px;top:237px"><svg width="34" height="34" viewBox="0 0 34 34"><rect x="3" y="6" width="22" height="20" fill="none" stroke="#111" stroke-width="2.5"/><circle cx="25" cy="24" r="7" fill="#fff" stroke="#111" stroke-width="2.5"/><path d="M25 20v4h3" stroke="#111" stroke-width="2" fill="none"/></svg></div>
  <div class="badge" style="left:356px;top:332px"><svg width="34" height="34" viewBox="0 0 34 34"><circle cx="17" cy="14" r="8" fill="#111"/><rect x="13" y="23" width="8" height="6" fill="#111"/></svg></div>
  <div class="badge" style="left:770px;top:332px"><svg width="34" height="34" viewBox="0 0 34 34"><circle cx="11" cy="11" r="5" fill="#111"/><circle cx="23" cy="19" r="5" fill="#111"/><rect x="4" y="18" width="12" height="8" rx="4" fill="#111"/><rect x="16" y="26" width="14" height="6" rx="3" fill="#111"/></svg></div>

  <div class="reason right" style="right:714px;top:160px"><h3>Unbiased Recommendations</h3><p>Lorem ipsum dolor sit mork<br>adipiscing sed diam</p></div>
  <div class="reason" style="left:700px;top:160px"><h3>Expert Guidance</h3><p>Lorem ipsum dolor sit mork<br>adipiscing sed diam</p></div>
  <div class="reason right" style="right:813px;top:254px"><h3>Unparalleled Service</h3><p>Lorem ipsum dolor sit mork<br>adipiscing sed diam</p></div>
  <div class="reason" style="left:805px;top:260px"><h3>Considerable Time For You</h3><p>Lorem ipsum dolor sit mork<br>adipiscing sed diam...[+]</p></div>
  <div class="reason right" style="right:863px;top:359px"><h3>Superior Advice</h3><p>Lorem ipsum dolor sit mork<br>adipiscing sed diam</p></div>
  <div class="reason" style="left:858px;top:345px"><h3>Deep Legal Industry<br>Relationships</h3><p>Lorem ipsum dolor sit mork<br>adipiscing sed diam...[+]</p></div>
</section>

<h2 class="abs script intro-title">Lorem Ispum is the Dummy Text</h2>
<p class="abs intro-body">Lorem ipsum dolor sit amet, consectetuer adipiscing elit, sed reederiam nonummy nibh euismod tincidunt ut laoreet dolore &nbsp;lor emsmagna aliquam erat volutpat. Ut wisi enim fdaad minim veniam, quis nostrud exerci tation ullamcorper suscipit lobortis nisl ut aliquip ex ea commodo consequat.</p>
<p class="abs script contact-line" style="top:2244px">Contact Us Today - 123.456.7890</p>

<div class="abs desk" role="img" aria-label="White desk from above with keyboard, potted plant, pencil and a cup of coffee"></div>
<section class="abs card">
  <h2 class="script">Do You Have A Question?</h2>
  <div class="bar"></div>
  <p>Lorem Ipsum is simply dummy text of the printing and typesetting industry. Lorem Ipsum has been the industry's standard dummy text ever since the 1500s.</p>
  <div class="field" style="left:56px;top:204px;width:268px;height:35px;padding-top:10px">Name</div>
  <div class="field" style="left:339px;top:204px;width:268px;height:35px;padding-top:10px">Email</div>
  <div class="field" style="left:56px;top:254px;width:551px;height:85px">Message</div>
  <div class="submit">SUBMIT <svg width="14" height="10"><path d="M0 5h12M8 1l4 4-4 4" stroke="#fff" stroke-width="1.4" fill="none"/></svg></div>
  <div class="fold"></div>
</section>

<footer class="abs site-footer">
  <div class="contact-item" style="left:142px">
    <svg width="18" height="22" viewBox="0 0 18 22"><path d="M9 0a8 8 0 0 1 8 8c0 6-8 14-8 14S1 14 1 8a8 8 0 0 1 8-8z" fill="#fff"/><circle cx="9" cy="8" r="3" fill="#1a1a1a"/></svg>
    <span>Street Name, City Name<br>State Zipcode</span>
  </div>
  <div class="contact-item" style="left:387px">
    <svg width="30" height="30" viewBox="0 0 26 26"><circle cx="13" cy="13" r="11.5" fill="none" stroke="#fff" stroke-width="1.6"/><path d="M10 7c-2 1-2 3-1 6s3 5 5 6c1 .4 2 0 3-1l-2-2-1 1c-1-.5-2-2-2.5-3l1-1-2-3z" fill="#fff"/></svg>
    <span>Call Us Today<br>&nbsp;&nbsp;123.456.7890</span>
  </div>
  <div class="contact-item" style="left:575px">
    <svg width="28" height="20" viewBox="0 0 28 20"><rect width="28" height="20" rx="2" fill="#fff"/><path d="M1 2l13 9 13-9" stroke="#1a1a1a" stroke-width="2" fill="none"/></svg>
    <span>Email<br>inquiry@bronasdwellings.com</span>
  </div>
  <div class="foot-brand"><span class="mark"></span>Brona's Dwellings</div>
</footer>

<div class="abs copy-bar">
  <span class="note">Copyright © 2018 Brona's Dwellings. &nbsp;All Rights Reserved.</span>
  <span class="social" style="left:920px;background:#3b5998"></span>
  <span class="social" style="left:957px;background:#1da1f2"></span>
  <span class="social" style="left:994px;background:#0077b5"></span>
  <span class="social" style="left:1031px;background:#dd4b39"></span>
</div>

</body>
</html>
```